House Church design model for faith-based organization

A design is needed for a house church model (Christian, faith-based). I’m looking for a graphic to convey four house church hallmarks showing the balance of member engagement. The four-part model includes - God’s Presence, Community, Discipleship, Outreach. The model should consist of the text for the four parts and the words - House Church

Perhaps a circular/modular design with House Church in the center. Using equally-sized interlocking slices or winged parts (graphically speaking, but not angelic wings) may help convey a balanced approach. It isn’t a process and should not appear in progressive steps, but the order (as listed) is used when explaining the concept. The model will be used for members to evaluate monthly focus.

I’m open to interpretation of the design and artwork. Designers should not feel a need to utilize cliché-like Christian symbols. However, if done minimally (and perhaps first century-like), they could be of interest (but are not required). Keeping it abstract may help readability and convey a roots/back-to-basics feel.

The artwork will be used for a video and PowerPoint presentation. It should be vector-based for simple movement/animation.

Additional thoughts:
Readable, not complex
Interesting interlocking design found at: https://www.pixelvarno.com/ring-module-infographic-choices-segments-stages-layout-loop-diagram-chart-round-graph-image507318264

Target Market(s)

To existing members (for reflection) and for those seeking a simpler church experience.

Requirements
Must have
• Simple, readable design, ability to reproduce for PowerPoint, video, and web. Prefer simple illustrations rather than images.
Nice to have
• The design should create a calming sense of focus on four priorities vs. the complexity of structure/requirements often found in the church experience.
Should not have
• Not crazy about puzzle pieces. Please avoid using all CAPS and serif fonts. Should not use complex images or photos.

```html
<!DOCTYPE html>
<html lang="en">
<head>
<meta charset="utf-8">
<title>House Church Model</title>
<link rel="stylesheet" href="https://fonts.googleapis.com/css2?family=Poppins:wght@600&display=swap">
<style>
  :root {
    --page-bg: #ffffff;
    --presence-edge: #17a99c;
    --presence-fill: #1b9d8e;
    --community-edge: #8cc63e;
    --community-fill: #7aab42;
    --outreach-edge: #f68b24;
    --outreach-fill: #e17427;
    --discipleship-edge: #ea4e3e;
    --discipleship-fill: #d63b33;
    --hub-fill: #1d5fa6;
    --label-color: #ffffff;
  }
  html, body {
    margin: 0;
    padding: 0;
    width: 1200px;
    height: 1200px;
    overflow: hidden;
    background: var(--page-bg);
  }
  .model {
    display: block;
    width: 1200px;
    height: 1200px;
  }
  .petal-edge { stroke-width: 26; stroke-linejoin: miter; }
  .petal--presence .petal-edge { fill: var(--presence-edge); stroke: var(--presence-edge); }
  .petal--presence .petal-fill { fill: var(--presence-fill); }
  .petal--community .petal-edge { fill: var(--community-edge); stroke: var(--community-edge); }
  .petal--community .petal-fill { fill: var(--community-fill); }
  .petal--outreach .petal-edge { fill: var(--outreach-edge); stroke: var(--outreach-edge); }
  .petal--outreach .petal-fill { fill: var(--outreach-fill); }
  .petal--discipleship .petal-edge { fill: var(--discipleship-edge); stroke: var(--discipleship-edge); }
  .petal--discipleship .petal-fill { fill: var(--discipleship-fill); }
  .hub-gap { fill: var(--page-bg); }
  .hub { fill: var(--hub-fill); }
  .label {
    font-family: "Poppins", sans-serif;
    font-weight: 600;
    font-size: 21px;
    fill: var(--label-color);
    text-anchor: middle;
  }
  .hub-label {
    font-family: "Poppins", sans-serif;
    font-weight: 600;
    font-size: 29px;
    fill: var(--label-color);
    text-anchor: middle;
  }
</style>
</head>
<body>
<svg class="model" viewBox="0 0 1080 1080" xmlns="http://www.w3.org/2000/svg" xmlns:xlink="http://www.w3.org/1999/xlink">
  <defs>
    <path id="petal-shape" d="M0,-325 L96.6,-228.4 A50,50 0 0 1 96.6,-157.6 L35.4,-96.4 A50,50 0 0 1 -35.4,-96.4 L-96.6,-157.6 A50,50 0 0 1 -96.6,-228.4 Z"/>
  </defs>

  <g transform="translate(563 525)">
    <g class="petal petal--presence">
      <use class="petal-edge" xlink:href="#petal-shape"/>
      <use class="petal-fill" xlink:href="#petal-shape"/>
    </g>
    <g class="petal petal--community" transform="rotate(90)">
      <use class="petal-edge" xlink:href="#petal-shape"/>
      <use class="petal-fill" xlink:href="#petal-shape"/>
    </g>
    <g class="petal petal--outreach" transform="rotate(180)">
      <use class="petal-edge" xlink:href="#petal-shape"/>
      <use class="petal-fill" xlink:href="#petal-shape"/>
    </g>
    <g class="petal petal--discipleship" transform="rotate(270)">
      <use class="petal-edge" xlink:href="#petal-shape"/>
      <use class="petal-fill" xlink:href="#petal-shape"/>
    </g>

    <circle class="hub-gap" r="84"/>
    <circle class="hub" r="72"/>
  </g>

  <text class="label" x="563" y="329">God’s</text>
  <text class="label" x="563" y="358">Presence</text>
  <text class="label" x="754" y="534">Community</text>
  <text class="label" x="567" y="707">Outreach</text>
  <text class="label" x="365" y="534">Discipleship</text>

  <text class="hub-label" x="563" y="516">House</text>
  <text class="hub-label" x="563" y="545">Church</text>
</svg>
</body>
</html>
```